Counseling Practice Business Card

I need a professional looking business card incorporating my new logo that was just completed. Card needs to incorporate my name and title, description of my specialty, my address, my phone number, my fax number, my email and my website URL. I need to be able to choose design on/with different paper colors and textures.
I do not have a lot of business card ideas so I am open to anything but I want bold,sharp, clear card without additional designs other than my logo (see attached file info). I am open to different color backgrounds or paper colors including black. I do not like traditional brackets around area codes in phone number or dashes between numbers in phone number. Am open to other ways of presenting including periods between numbers as appropriate. I do not know enough to know what I like yet but I want card to coordinate and work together with my logo. My practice emphasizes natural mental health interventions so any use of color (with background paper color or the blue and green in my logo) that elicits nature is nice. In addition to black, any natural brown or wood looking background might be desirable also. Most of the offerings so far look very similar and boring.

Target Market(s)

Potential therapy clients and other professionals

Contact Information for Business Card

Card information:
Marcus T. Whitfield, Ph.D.
Licensed Clinical Psychologist
Integrative Health Coach
4812 Ferndale Pkwy NW
Suite 730
Duluth, GA 30096
770.555.0142 phone
770.555.0186 fax
drmarcuswhitfield@kelvora.com
pathbloomcounseling.com

Font styles to use
Serif
Sans Serif
Other font styles liked:
• anything that you think looks crisp, clear and easily readable

Requirements
Must have
• Any color used should coordinate with my logo design (see attached files).
• Card should be printed horizontally so top and bottom are longest sides of rectangle.
• Background color or paper color should complement and highlight logo. Do not like a white background. black, grey, brown or any color my logo would blend well with.
Nice to have
• I would like designer to utilize color to highlight letters/name or phone-fax-web symbols.
• Bottom edge of card could be highlighted if appropriate to an idea.
Should not have
• I would NOT want the card to have a pure white background at all.
• No clear cards.
• Cards should be oriented with long sides on bottom and top, NOT sides. DO NOT LIKE THIS THIN TALL ORIENTATION.

```html
<!DOCTYPE html>
<html lang="en">
<head>
<meta charset="utf-8">
<title>Marcus T. Whitfield, Ph.D. – Business Card</title>
<link href="https://fonts.googleapis.com/css2?family=Barlow:wght@400;500;600&display=swap" rel="stylesheet">
<style>
  :root {
    --red-orange: #F15A29;
    --orange: #F7941D;
    --triangle: #F8A12A;
    --card-grey: #E9E8EC;
    --card-light: #F2F1F4;
    --map-tone: #DCDBE0;
    --ink: #231F20;
    --divider: #C1272D;
    --page: #FFFFFF;
  }
  * { margin: 0; padding: 0; box-sizing: border-box; }
  html, body {
    width: 1200px; height: 1000px; overflow: hidden;
    background: var(--page);
    font-family: "Barlow", "Helvetica Neue", Arial, sans-serif;
    color: var(--ink);
  }
  .card {
    position: absolute; left: 166px; top: 252px;
    width: 868px; height: 496px;
    background: var(--card-grey);
    overflow: hidden;
  }
  .card-art { position: absolute; inset: 0; }
  .band { position: absolute; height: 49px; width: 434px; }
  .band--top-left { top: 0; left: 0; background: var(--red-orange); }
  .band--top-right { top: 0; left: 434px; background: var(--orange); }
  .band--bottom-left { bottom: 0; left: 0; height: 50px; background: var(--orange); }
  .band--bottom-right { bottom: 0; left: 434px; height: 50px; background: var(--red-orange); }

  .brand {
    position: absolute; left: 50px; top: 132px;
    display: flex; align-items: center; gap: 9px;
  }
  .brand__mark {
    width: 26px; height: 26px; border-radius: 50%;
    background: var(--red-orange);
  }
  .brand__name {
    font-size: 18px; font-weight: 600; letter-spacing: 0.3px;
    color: var(--red-orange); white-space: nowrap;
  }

  .identity { position: absolute; left: 50px; top: 198px; }
  .identity__name {
    font-size: 33px; font-weight: 500; letter-spacing: 0.3px;
    line-height: 40px; white-space: nowrap;
  }
  .identity__rule {
    width: 109px; height: 2px; background: var(--orange); margin-top: 1px;
  }
  .identity__title {
    margin-top: 9px; font-size: 20.5px; line-height: 25px; font-weight: 400;
    letter-spacing: 0.2px;
  }

  .contact {
    position: absolute; right: 86px; top: 146px;
    text-align: right; font-size: 20px; font-weight: 400; line-height: 25px;
    list-style: none;
  }
  .contact li { height: 40.5px; white-space: nowrap; }
  .contact li.contact__address { height: auto; margin-top: -5px; }

  .icon-strip {
    position: absolute; left: 794px; top: 120px;
    width: 50px; height: 252px; background: var(--red-orange);
  }
</style>
</head>
<body>
  <div class="card">
    <svg class="card-art" width="868" height="496" viewBox="0 0 868 496">
      <rect role="img" aria-label="Faint dotted world map spanning the card background" x="48" y="53" width="745" height="390" rx="30" fill="var(--map-tone)" opacity="0.45"/>
      <polygon points="654,49 868,49 868,446 309,446" fill="var(--card-light)" opacity="0.9"/>
      <polygon points="282,116 346,133 299,180" fill="none" stroke="var(--triangle)" stroke-width="3"/>
      <polygon points="302,340 400,314 374,411" fill="none" stroke="var(--orange)" stroke-width="3"/>
      <path d="M71,377 C80,368 87,366 94,373 C101,381 106,383 114,375 C121,368 128,368 134,374 C140,381 145,381 146,374" fill="none" stroke="var(--red-orange)" stroke-width="3" stroke-linecap="round"/>
    </svg>

    <div class="band band--top-left"></div>
    <div class="band band--top-right"></div>
    <div class="band band--bottom-left"></div>
    <div class="band band--bottom-right"></div>

    <div class="brand">
      <span class="brand__mark"></span>
      <span class="brand__name">Pathbloom Counseling</span>
    </div>

    <div class="identity">
      <h1 class="identity__name">Marcus T. Whitfield, Ph.D.</h1>
      <div class="identity__rule"></div>
      <p class="identity__title">Licensed Clinical Psychologist /<br>Integrative Health Coach</p>
    </div>

    <ul class="contact">
      <li class="contact__phone">770.555.0142</li>
      <li class="contact__fax">770.555.0186</li>
      <li class="contact__email">drmarcuswhitfield@kelvora.com</li>
      <li class="contact__web">pathbloomcounseling.com</li>
      <li class="contact__address">4812 Ferndale Pkwy NW<br>Suite 730, Duluth, GA 30096</li>
    </ul>

    <svg class="icon-strip" width="50" height="252" viewBox="0 0 50 252" aria-hidden="true">
      <g stroke="var(--divider)" stroke-width="1.5">
        <line x1="12" y1="59" x2="37" y2="59"/>
        <line x1="12" y1="100" x2="37" y2="100"/>
        <line x1="12" y1="140" x2="37" y2="140"/>
        <line x1="12" y1="181" x2="37" y2="181"/>
      </g>
      <g fill="#FFFFFF">
        <path d="M16,31 C16,42 24,48 32,48 L35,45 L31,41 L28,43 C25,42 22,39 21,36 L23,33 L19,28 Z"/>
        <rect x="15" y="71" width="5" height="19" rx="1.5"/>
        <path d="M21,73 h8 l5,4 v13 h-13 z"/>
        <g fill="var(--red-orange)">
          <rect x="24" y="80" width="2" height="2"/><rect x="28" y="80" width="2" height="2"/>
          <rect x="24" y="84" width="2" height="2"/><rect x="28" y="84" width="2" height="2"/>
        </g>
        <rect x="14" y="112" width="21" height="16" rx="1.5"/>
        <path d="M14,113 L24.5,121 L35,113" fill="none" stroke="var(--red-orange)" stroke-width="1.6"/>
        <circle cx="24.5" cy="160" r="10"/>
        <g fill="none" stroke="var(--red-orange)" stroke-width="1.3">
          <ellipse cx="24.5" cy="160" rx="4.2" ry="10"/>
          <line x1="14.5" y1="160" x2="34.5" y2="160"/>
          <path d="M16,155 h17 M16,165 h17"/>
        </g>
        <path d="M13,201 L24.5,191 L36,201 L34,203 L24.5,195 L15,203 Z"/>
        <path d="M17,202 L24.5,196 L32,202 V211 H27 V205 H22 V211 H17 Z"/>
      </g>
    </svg>
  </div>
</body>
</html>
```